Military and tactical gear supply company needs web design

We need a web design for a company called U.S. Ravenfield. We provide quality tactical equipment to military and law enforcement. This is an e-commerce business and we primarily market ourselves on social media. Our key products are backpacks, military-style belts, and tactical flashlights. The gear we sell is not yet widely known about, but is on par with the state-of-the-art products in this field. We want the website to convey the message of quality, durability, and reliability. We use the word "kinetic" because the customers in this field are very "action-oriented" and we would like that idea to be communicated in the web site as well. The primary demographic is men in their 20's-30's, so the web site should have a masculine feel to it. Attached is the logo and color scheme.

```html
<!DOCTYPE html>
<html lang="en">
<head>
<meta charset="utf-8">
<title>U.S. Ravenfield – Tactical Gear</title>
<link href="https://fonts.googleapis.com/css2?family=Saira:wght@400;500;600;700;800&family=Catamaran:wght@400;500;600&display=swap" rel="stylesheet">
<style>
:root{
  --red:#9b0c17;
  --blue:#2a5677;
  --blue-text:#2e5f86;
  --nav-active:#3b6f95;
  --grey-bg:#e7e7e7;
  --grey-btn:#7d7d7d;
  --dark:#0f1317;
  --text:#333;
  --white:#fff;
}
*{margin:0;padding:0;box-sizing:border-box}
html,body{width:1200px;height:3272px;overflow:hidden}
body{position:relative;background:var(--white);font-family:"Catamaran",sans-serif;color:var(--text)}
.abs{position:absolute}
.heading{font-family:"Saira",sans-serif;font-weight:700;color:var(--red);text-align:center;font-size:40px;line-height:1}

/* header */
.brand{left:145px;top:30px;font-family:"Saira",sans-serif;font-weight:800;font-size:40px;color:var(--blue);letter-spacing:.5px;line-height:1}
.brand-url{left:305px;top:70px;font-family:"Saira",sans-serif;font-size:17px;font-weight:600;color:#222;line-height:1}
.search{left:747px;top:24px;width:240px;height:39px;border:1px solid #bbb;padding:0 15px;display:flex;align-items:center;justify-content:space-between;font-size:14px;color:#888}
.cart{left:1015px;top:24px;width:40px;height:40px;border-radius:50%;background:var(--blue);display:flex;align-items:center;justify-content:center}
.cart-count{left:1004px;top:25px;width:18px;height:18px;border-radius:50%;background:#222;color:#fff;font-size:10px;display:flex;align-items:center;justify-content:center;border:2px solid #fff}
.nav{top:78px;left:509px;display:flex;gap:0;font-family:"Saira",sans-serif;font-size:16px;color:#222}
.nav a{text-decoration:none;color:inherit;position:absolute;white-space:nowrap}
.nav a.active{color:var(--nav-active)}

/* hero */
.hero-title{right:143px;top:170px;font-family:"Saira",sans-serif;font-weight:700;font-size:33px;color:#fff;white-space:nowrap}
.shop-btn{left:919px;top:230px;width:136px;height:46px;background:var(--red);color:#fff;font-family:"Saira",sans-serif;font-weight:700;font-size:19px;display:flex;align-items:center;justify-content:center}
.arrow{top:346px;width:40px;height:40px;background:#e9e9e9;display:flex;align-items:center;justify-content:center}

/* welcome */
.intro{left:145px;top:750px;width:910px;text-align:center;font-size:15.5px;line-height:27px;color:#444}
.cat{background:#555}
.cat-label{right:15px;text-align:right;color:#fff}
.cat-label b{display:block;font-family:"Saira",sans-serif;font-weight:700;font-size:33px;line-height:1}
.cat-label span{display:block;font-size:13.5px;margin-top:6px}

/* products */
.filters{top:1534px;left:0;width:1200px;text-align:center;font-family:"Saira",sans-serif;font-size:24px;color:#555}
.filters .on{color:var(--red);text-decoration:underline;text-underline-offset:5px}
.filters i{font-style:normal;margin:0 16px}
.product{top:1596px;width:217px;height:239px;background:#fff}
.product .ph{height:176px}
.product p{text-align:center;font-size:15.5px;line-height:21px;padding-top:11px;color:#444}

/* news */
.news{top:2122px;width:289px;height:368px;background:#e7e7e7}
.news .ph{height:192px}
.date{left:16px;top:158px;width:55px;height:65px;background:var(--blue);color:#fff;font-family:"Saira",sans-serif;font-weight:700;text-align:center;line-height:1}
.date b{display:block;font-size:36px;margin-top:2px}
.date span{display:block;font-size:20px;margin-top:-3px}
.news h3{position:absolute;left:16px;top:246px;width:262px;font-family:"Saira",sans-serif;font-weight:400;font-size:15.5px;line-height:22px;color:var(--blue-text)}
.news p{position:absolute;left:16px;top:296px;width:262px;font-size:10.5px;line-height:17.5px;color:#444}
.view-all{left:532px;top:2516px;width:136px;height:48px;background:var(--grey-btn);color:#fff;font-family:"Saira",sans-serif;font-weight:700;font-size:19px;display:flex;align-items:center;justify-content:center}

/* newsletter */
.nl-title{left:143px;top:2765px;text-align:left}
.nl-text{left:145px;top:2816px;width:420px;font-size:16px;line-height:27px;color:#333}
.nl-input{left:145px;top:2887px;width:410px;height:55px;border:1px solid #aaa;background:#fff;padding:0 18px;display:flex;align-items:center;font-size:15px;color:#666}
.nl-btn{left:145px;top:2961px;width:135px;height:47px;background:var(--blue);color:#fff;font-family:"Saira",sans-serif;font-weight:700;font-size:19px;display:flex;align-items:center;justify-content:center}

/* footer */
.foot-brand{left:820px;top:3104px;font-family:"Saira",sans-serif;font-weight:800;font-size:30px;color:#9aa3ab;line-height:1}
.foot-links{left:145px;top:3184px;font-size:11.5px;color:#c9ced3}
.foot-links i{font-style:normal;margin:0 9px;color:#777}
.copy{left:145px;top:3220px;font-size:11.5px;color:#c9ced3}
.social{top:3200px;width:20px;height:20px;background:#6f8596;border-radius:2px}
</style>
</head>
<body>

<!-- header -->
<div class="abs brand">U.S. Ravenfield</div>
<div class="abs brand-url">usravenfield.com</div>
<div class="abs search">Search
  <svg width="15" height="15" viewBox="0 0 15 15"><circle cx="6" cy="6" r="4.5" fill="none" stroke="#2a5677" stroke-width="2"/><line x1="9.5" y1="9.5" x2="14" y2="14" stroke="#2a5677" stroke-width="2.2"/></svg>
</div>
<div class="abs cart">
  <svg width="18" height="16" viewBox="0 0 18 16"><path d="M1 2h3l2 8h9l2-6H5" fill="none" stroke="#fff" stroke-width="2"/><circle cx="7" cy="13.5" r="1.6" fill="#fff"/><circle cx="14" cy="13.5" r="1.6" fill="#fff"/></svg>
</div>
<div class="abs cart-count">0</div>
<nav class="abs nav" style="left:0;width:1200px;height:24px">
  <a class="active" style="left:509px">Home</a>
  <a style="left:591px">About Us</a>
  <a style="left:696px">Products</a>
  <a style="left:799px">Services</a>
  <a style="left:899px">News</a>
  <a style="left:978px">Contact Us</a>
</nav>

<!-- hero -->
<svg class="abs" style="left:0;top:118px" width="1200" height="510" viewBox="0 0 1200 510">
  <defs>
    <linearGradient id="heroFill" x1="0" y1="0" x2="1" y2="1">
      <stop offset="0" stop-color="#5a3a28"/>
      <stop offset=".5" stop-color="#3a2a22"/>
      <stop offset="1" stop-color="#1c1c1e"/>
    </linearGradient>
  </defs>
  <polygon points="0,0 1200,0 1200,436 606,436 575,497 0,497" fill="url(#heroFill)" role="img" aria-label="Two tactical flashlights lit up on a weathered wooden table beside a nylon pouch"/>
  <polyline points="1200,437 607,437 576,498" fill="none" stroke="#9b0c17" stroke-width="6"/>
  <line x1="0" y1="501" x2="568" y2="501" stroke="#2a5677" stroke-width="7"/>
</svg>
<div class="abs hero-title">Quality • Durability • Reliability</div>
<div class="abs shop-btn">SHOP NOW</div>
<div class="abs arrow" style="left:51px"><svg width="16" height="20" viewBox="0 0 16 20"><polyline points="12,2 4,10 12,18" fill="none" stroke="#222" stroke-width="4"/></svg></div>
<div class="abs arrow" style="left:1107px"><svg width="16" height="20" viewBox="0 0 16 20"><polyline points="4,2 12,10 4,18" fill="none" stroke="#222" stroke-width="4"/></svg></div>

<!-- welcome -->
<h1 class="abs heading" style="left:0;top:698px;width:1200px">Welcome to U.S. Ravenfield</h1>
<p class="abs intro">Nulla in lorem at massa pellentesque posuere. Nulla tristique posuere molestie. Aliquam erat volutpat. Etiam quis aliquet risus. Duis ornare erat eget magna dapibus, in accumsan quam pharetra. Nam tempus, quam in bibendum vulputate, sapien dolor viverra nisl, vitae euismod elit turpis et nulla. Aliquam erat volutpat. Pellentesque blandit lacus eget nunc faucibus.</p>

<div class="abs cat" style="left:145px;top:859px;width:450px;height:459px;background:linear-gradient(160deg,#5c5e44,#3a3d2e 55%,#23251f)" role="img" aria-label="Soldier in camouflage gripping the shoulder straps of a backpack"></div>
<div class="abs cat" style="left:605px;top:859px;width:450px;height:223px;background:linear-gradient(135deg,#3f4652,#2b3548 55%,#6e6a5e)" role="img" aria-label="Close-up of a military-style belt buckle"></div>
<div class="abs cat" style="left:605px;top:1094px;width:450px;height:224px;background:radial-gradient(ellipse at 55% 40%,#8a7040,#2b2418 45%,#0d0c0b)" role="img" aria-label="Metal tactical flashlight on a dark background"></div>

<svg class="abs" style="left:145px;top:1242px" width="450" height="76"><polygon points="40,0 450,0 450,76 0,76" fill="#2a5677" fill-opacity=".88"/></svg>
<svg class="abs" style="left:605px;top:1001px" width="450" height="81"><polygon points="40,0 450,0 450,81 0,81" fill="#2a5677" fill-opacity=".88"/></svg>
<svg class="abs" style="left:605px;top:1238px" width="450" height="80"><polygon points="40,0 450,0 450,80 0,80" fill="#2a5677" fill-opacity=".88"/></svg>

<div class="abs cat-label" style="right:622px;top:1253px"><b>BACKPACKS</b><span>Phasellus consequat sagittis nisi suscipit feugiat  nunc hendrerit.</span></div>
<div class="abs cat-label" style="right:162px;top:1012px"><b>MILITARY-STYLE BELTS</b><span>Maecenas consequat justo enim, ac mattis massa imperdiet quis</span></div>
<div class="abs cat-label" style="right:162px;top:1253px"><b>TACTICAL FLASHLIGHTS</b><span>Sed augue orci elementum in magna congue tincidunt vulputate</span></div>

<!-- products -->
<svg class="abs" style="left:0;top:1398px" width="1200" height="592">
  <polygon points="0,0 1200,0 1200,585 632,585 600,518 0,518" fill="#e7e7e7"/>
  <polyline points="0,520 600,520 632,585" fill="none" stroke="#9b0c17" stroke-width="6"/>
  <line x1="632" y1="586" x2="1200" y2="586" stroke="#2a5677" stroke-width="7"/>
</svg>
<h2 class="abs heading" style="left:0;top:1473px;width:1200px">Our Products</h2>
<div class="abs filters"><span class="on">All</span><i>|</i>Backpacks<i>|</i>Military-style belts<i>|</i>Tactical flashlights</div>

<div class="abs product" style="left:145px"><div class="ph" style="background:linear-gradient(180deg,#4d6b3a,#3b4a36 55%,#8a7a52)" role="img" aria-label="Backpack resting on a riverbank"></div><p>Aliquam consectetur<br>orci diam</p></div>
<div class="abs product" style="left:376px"><div class="ph" style="background:linear-gradient(150deg,#8c7a55,#6e5c3c 50%,#a48d62)" role="img" aria-label="Coiled khaki webbing belt"></div><p>Vestibulum condimentum<br>risus ut</p></div>
<div class="abs product" style="left:607px"><div class="ph" style="background:linear-gradient(180deg,#6a8a3e,#3e4d2e 50%,#7b7d80)" role="img" aria-label="Black flashlight on a rock outdoors"></div><p>Proin placerat dapibus<br>gravida</p></div>
<div class="abs product" style="left:838px"><div class="ph" style="background:linear-gradient(160deg,#4e4236,#2c2620 60%,#1a1816)" role="img" aria-label="Person in tactical clothing carrying a backpack"></div><p>Maecenas vel tortor<br>accumsan quam</p></div>

<!-- news -->
<h2 class="abs heading" style="left:0;top:2064px;width:1200px">News</h2>

<article class="abs news" style="left:145px">
  <div class="ph" style="background:radial-gradient(circle at 45% 45%,#3c4a40,#121414 45%,#0a0a0a)" role="img" aria-label="Gloved hand holding a glowing flashlight in the dark"></div>
  <div class="abs date"><b>25</b><span>JUL</span></div>
  <h3>Etiam elementum bibendum tellus venenatis feugiat massa.</h3>
  <p>Vivamus lacus justo, ultrices nec erat in, euismod iaculis mauris. Vivamus eleifend vitae nulla vel male-suada vitae lectus sit amet.</p>
</article>
<article class="abs news" style="left:456px">
  <div class="ph" style="background:linear-gradient(180deg,#6f6650,#8a7452 50%,#5d5a45)" role="img" aria-label="Tan tactical belt worn over camouflage trousers"></div>
  <div class="abs date"><b>25</b><span>JUL</span></div>
  <h3>Cras augue magna placerat eget nulla congue suscipit neque</h3>
  <p>Vivamus lacus justo, ultrices nec erat in, euismod iaculis mauris. Vivamus eleifend vitae nulla vel male-suada vitae lectus sit amet.</p>
</article>
<article class="abs news" style="left:767px">
  <div class="ph" style="background:linear-gradient(160deg,#6a7a3a,#7d7d6e 50%,#4e5a34)" role="img" aria-label="Camouflage backpack standing in grass"></div>
  <div class="abs date"><b>25</b><span>JUL</span></div>
  <h3>Praesent iaculis faucibus urna sit amet lacinia consequat justo.</h3>
  <p>Vivamus lacus justo, ultrices nec erat in, euismod iaculis mauris. Vivamus eleifend vitae nulla vel male-suada vitae lectus sit amet.</p>
</article>
<div class="abs view-all">VIEW ALL</div>

<!-- newsletter -->
<div class="abs" style="left:0;top:2645px;width:600px;height:500px;background:var(--grey-bg)"></div>
<div class="abs" style="left:600px;top:2645px;width:600px;height:432px;background:linear-gradient(150deg,#3a3c42,#24262b 50%,#4a4b50)" role="img" aria-label="Flat lay of a watch, flashlight, multitool and webbing straps on a dark surface"></div>
<h2 class="abs heading nl-title">Newsletter Sign Up</h2>
<p class="abs nl-text">Vestibulum ante ipsum primis in faucibus orci luctus et ultrices posuere cubilia.</p>
<div class="abs nl-input">Email Address</div>
<div class="abs nl-btn">SUBSCRIBE</div>

<!-- footer -->
<svg class="abs" style="left:0;top:3070px" width="1200" height="202">
  <polygon points="600,5 1200,5 1200,202 0,202 0,72 570,72" fill="#0f1317"/>
  <polyline points="1200,6 601,6 571,70" fill="none" stroke="#9b0c17" stroke-width="6"/>
  <line x1="0" y1="73" x2="566" y2="73" stroke="#2a5677" stroke-width="7"/>
</svg>
<div class="abs foot-brand">U.S. Ravenfield</div>
<div class="abs foot-links">Home<i>|</i>About Us<i>|</i>Products<i>|</i>Services<i>|</i>News<i>|</i>Contact Us<i>|</i>My Account<i>|</i>My Cart<i>|</i>Wishlist<i>|</i>Checkout</div>
<div class="abs copy">Copyright © 2020 &nbsp;U.S. Ravenfield. &nbsp;All rights reserved.</div>
<div class="abs social" style="left:991px"></div>
<div class="abs social" style="left:1034px"></div>

</body>
</html>
```